Broschüre für unsere Firma
Zielgruppe
Wäscherei Kranzbeck / Textilservice
Geschäftskunden
Logos etc. In OneDrive/ Dropbox
https://ablage-beispiel.de/f/s!XkrTmWq7PzvoNeFgHsYa4Lc92_p
Wir wollen gerne eine 4 seitige Broschüre erstellen lassen, um unsere Firma vorzustellen.
Insbesondere der Service
Berufsbekleidung
Hygiene Gardienenwäsche Service
Hotelmietwäsche
Mitbewerb
http://www.wäscherei-gollwitz.de/index.php/ct-menu-item-17/ct-menu-item-25
http://www.tuch-morgen.ch/download
Im Anhang finden Sie Bilder Logo und Flyers welche wir mal selbst gemacht haben!
Datein sind im OneDrive
Aufgabenstellung

```html
<!DOCTYPE html>
<html lang="de">
<head>
<meta charset="utf-8">
<title>Wäscherei Kranzbeck – Broschüre</title>
<link rel="stylesheet" href="https://fonts.googleapis.com/css2?family=Marcellus&family=Open+Sans:wght@300;400;700&display=swap">
<style>
  :root {
    --navy: #1b3c6e;
    --navy-deep: #16325e;
    --lime: #b5cc22;
    --lime-dark: #7ea12a;
    --yellow: #d8dc1e;
    --cyan: #0f9ad6;
    --hex-blue: #1583c4;
    --lavender: #6f7aa8;
    --lavender-light: #c7cbe2;
    --gold: #ebc56c;
    --ink: #16284a;
    --white: #ffffff;
  }
  * { margin: 0; padding: 0; box-sizing: border-box; }
  html, body { width: 1060px; height: 1200px; overflow: hidden; background: var(--white); }
  .canvas { position: relative; width: 1060px; height: 1200px; }
  .page { position: absolute; display: block; }
  .cover { left: 289px; top: 75px; width: 485px; height: 342px; }
  .spread { left: 47px; top: 434px; width: 971px; height: 342px; }
  .back { left: 297px; top: 797px; width: 485px; height: 342px; }
  .serif { font-family: "Marcellus", serif; }
  .sans { font-family: "Open Sans", sans-serif; }
  .body-copy { font-family: "Open Sans", sans-serif; font-weight: 300; font-size: 10.5px; }
  .brand-name { font-family: "Open Sans", sans-serif; font-weight: 700; }
</style>
</head>
<body>
<div class="canvas">

  <!-- Front cover -->
  <svg class="page cover" viewBox="0 0 596 420" xmlns="http://www.w3.org/2000/svg">
    <rect width="596" height="420" fill="var(--navy)"/>
    <polygon points="40,50 52,28 78,28 90,50 78,72 52,72" fill="#8a8a5a" opacity=".8"/>
    <polygon points="55,95 80,52 122,52 147,95 122,138 80,138" fill="var(--hex-blue)" opacity=".85"/>
    <polygon points="98,210 122,170 168,170 192,210 168,250 122,250" fill="var(--lavender)" opacity=".8"/>
    <polygon points="455,195 490,135 560,135 595,195 560,262 490,262" fill="#2d5f9c" opacity=".8"/>
    <polygon points="330,300 360,245 450,245 480,300 450,345 360,345" fill="#22477f" opacity=".7"/>
    <polygon points="148,135 228,-4 404,-4 480,135 404,296 218,296" fill="#0b0f1a"/>
    <g role="img" aria-label="Foto: rote und gelbe Waschmaschinen in einem Waschsalon">
      <defs>
        <linearGradient id="laundryPhoto" x1="0" x2="1" y1="0" y2="0">
          <stop offset="0" stop-color="#d8302a"/>
          <stop offset=".5" stop-color="#c9362c"/>
          <stop offset=".58" stop-color="#d9d04a"/>
          <stop offset="1" stop-color="#c6c448"/>
        </linearGradient>
      </defs>
      <polygon points="158,135 236,0 420,0 500,135 420,275 236,275" fill="url(#laundryPhoto)"/>
    </g>
    <polygon points="445,0 596,0 596,133 520,133" fill="var(--lime)"/>
    <polygon points="400,0 445,0 522,133 440,275 398,275 478,135" fill="var(--cyan)"/>
    <polygon points="0,318 292,318 352,420 0,420" fill="var(--lavender-light)"/>
    <rect x="310" y="354" width="286" height="48" fill="#2a5a9a" opacity=".85"/>
    <circle cx="43" cy="350" r="18" fill="var(--navy)"/>
    <text x="70" y="357" class="brand-name" font-size="19" fill="var(--navy)">Wäscherei Kranzbeck</text>
    <text x="25" y="395" class="sans" font-size="11.5" fill="var(--ink)">www.waescherei-kranzbeck.de</text>
    <text x="563" y="374" class="serif" font-size="17" fill="var(--white)" text-anchor="end">WO QUALITÄT</text>
    <text x="563" y="397" class="serif" font-size="17" fill="var(--white)" text-anchor="end">BESTIMMEDND IST</text>
  </svg>

  <!-- Inner spread -->
  <svg class="page spread" viewBox="0 0 1191 420" xmlns="http://www.w3.org/2000/svg">
    <defs>
      <linearGradient id="greenPanel" x1="0" x2="0" y1="0" y2="1">
        <stop offset="0" stop-color="#c3d22a"/>
        <stop offset="1" stop-color="#739a2a"/>
      </linearGradient>
    </defs>
    <rect width="1191" height="420" fill="var(--navy)"/>
    <rect x="460" width="472" height="420" fill="url(#greenPanel)"/>
    <rect x="456" width="4" height="420" fill="var(--lavender-light)" opacity=".6"/>
    <rect x="930" width="5" height="420" fill="var(--lavender-light)" opacity=".6"/>

    <!-- decorative hexagons -->
    <polygon points="302,52 320,18 360,18 378,52 360,86 320,86" fill="var(--hex-blue)"/>
    <polygon points="345,84 353,70 371,70 379,84 371,98 353,98" fill="var(--lavender)"/>
    <polygon points="322,188 333,169 358,169 369,188 358,209 333,209" fill="var(--hex-blue)"/>
    <polygon points="284,181 290,172 300,172 306,181 300,190 290,190" fill="var(--hex-blue)"/>
    <polygon points="302,264 308,254 320,254 326,264 320,274 308,274" fill="var(--lavender)"/>
    <polygon points="230,420 250,380 295,380 315,420" fill="var(--lavender)" opacity=".9"/>
    <polygon points="492,0 640,0 610,70 522,70" fill="var(--yellow)"/>
    <polygon points="650,0 735,0 714,40 672,40" fill="#dfe58f" opacity=".8"/>
    <polygon points="786,56 795,42 812,42 821,56 812,70 795,70" fill="#dfe58f" opacity=".8"/>
    <polygon points="823,99 835,78 860,78 872,99 860,120 835,120" fill="#1fae9a"/>
    <polygon points="905,168 911,157 923,157 929,168 923,179 911,179" fill="#c7d88a" opacity=".8"/>
    <polygon points="542,420 568,352 648,352 696,420" fill="var(--yellow)"/>
    <polygon points="620,295 628,281 646,281 654,295 646,309 628,309" fill="#cfdc9a" opacity=".8"/>
    <polygon points="832,357 840,344 856,344 864,357 856,370 840,370" fill="#d0de9a" opacity=".9"/>
    <polygon points="556,287 562,275 578,275 584,287 578,299 562,299" fill="var(--lavender)" opacity=".7"/>
    <polygon points="1130,25 1142,4 1166,4 1178,25 1166,46 1142,46" fill="var(--hex-blue)"/>
    <polygon points="1115,32 1122,20 1138,20 1145,32 1138,44 1122,44" fill="var(--lavender)"/>
    <polygon points="1132,375 1139,361 1157,361 1164,375 1157,389 1139,389" fill="var(--lavender)"/>
    <polygon points="940,420 952,385 1028,385 1040,420" fill="var(--lavender)" opacity=".8"/>

    <!-- service hexagons -->
    <polygon points="328,287 393,175 523,175 588,287 523,400 393,400" fill="#2b1f4c" opacity=".85"/>
    <polygon points="622,287 688,146 818,146 884,287 818,375 688,375" fill="#4f5a2c" opacity=".55"/>
    <polygon points="892,287 957,146 1107,146 1172,287 1107,400 957,400" fill="#272a5c" opacity=".85"/>

    <g role="img" aria-label="Foto: lächelnder Arzt im weißen Kittel">
      <polygon points="405,120 448,45 534,45 577,120 534,195 448,195" fill="#dfe6ee" stroke="var(--white)" stroke-width="2"/>
    </g>
    <g role="img" aria-label="Foto: Frau bezieht ein Hotelbett mit weißer Wäsche">
      <polygon points="622,120 665,45 752,45 795,120 752,195 665,195" fill="#e7cdbf" stroke="var(--white)" stroke-width="2"/>
    </g>
    <g role="img" aria-label="Foto: Mitarbeiterin in roter Kleidung vor Waschmaschinen">
      <polygon points="942,120 985,45 1072,45 1115,120 1072,195 985,195" fill="#c9a8a6" stroke="var(--white)" stroke-width="2"/>
    </g>

    <!-- Über uns -->
    <text x="42" y="42" class="serif" font-size="22" fill="var(--white)">ÜBER UNS</text>
    <text x="42" y="86" class="serif" font-size="25" fill="var(--lime)">Testen Sie uns und</text>
    <text x="42" y="113" class="serif" font-size="25" fill="var(--lime)">überzeugen Sie sich</text>
    <rect x="42" y="140" width="348" height="2" fill="var(--hex-blue)"/>
    <g class="body-copy" fill="var(--lavender-light)">
      <text x="42" y="169">Inimet aut eos erumeniateni dus sande</text>
      <text x="42" y="183.5">nonsers persped eum que et quistia</text>
      <text x="42" y="198">simusap erchicil ea aliquia dolorrum</text>
      <text x="42" y="212.5">cone labore nimus, corpori busanis rem</text>
      <text x="42" y="227">harum enimaionsedi con pliqui tecteca</text>
      <text x="42" y="241.5">borumqui nus magnatiis maximent.</text>
      <text x="42" y="256">Cupta quam esto velendam voluptaquia</text>
      <text x="42" y="270.5">pos rem que nat.</text>
      <text x="42" y="285">Parciis es deriber spietus nus oellit, quis</text>
      <text x="42" y="299.5">doloribuscit doluptatem quatur, conem-</text>
      <text x="42" y="314">poria dolupta sam nam net, cor site pe-</text>
      <text x="42" y="328.5">nonsequiatem quam acea adicide dnisto</text>
      <text x="42" y="343">blatibus as eturempore di siminum qua-</text>
      <text x="42" y="357.5">tionem harum hariam at utaeper eperia</text>
      <text x="42" y="372">etur, ut utaepel inum andit volorror ma</text>
      <text x="42" y="386.5">non</text>
    </g>

    <!-- Berufsbekleidung -->
    <text x="399" y="224" class="serif" font-size="16.5" fill="var(--gold)">Berufsbekleidung</text>
    <g class="body-copy" fill="var(--lavender-light)" font-size="10">
      <text x="392" y="248">Wenn es um die Sicherheit</text>
      <text x="392" y="260">Ihrer Mitarbeiter geht, über-</text>
      <text x="392" y="272">lassen Sie nichts dem Zufall.</text>
      <text x="392" y="284">Erfüllen Sie gemeinsam mit</text>
      <text x="392" y="296">uns die aktuellen BGTV Richt-</text>
      <text x="392" y="308">linien. Gerne stehen wir Ihnen</text>
      <text x="392" y="320">mit unserer kompetenten</text>
      <text x="392" y="332">persönlichen Beratungsteam</text>
      <text x="392" y="344">bei der Beschaffung und pro-</text>
      <text x="392" y="356">fessionellen Textilpflege zur</text>
      <text x="392" y="368">Verfügung.</text>
    </g>

    <!-- Hygiene -->
    <text x="679" y="220" class="serif" font-size="16.5" fill="var(--gold)">Hygiene Gardienen-</text>
    <text x="679" y="240" class="serif" font-size="16.5" fill="var(--gold)">wäsche Service</text>
    <g class="body-copy" fill="var(--lavender-light)" font-size="10">
      <text x="679" y="264">Lor suscipsam quunde si-</text>
      <text x="679" y="276">maionse natet peciorem</text>
      <text x="679" y="288">enimolum num voluptatur?</text>
      <text x="679" y="300">Odiam ex erum ad es eratquis</text>
      <text x="679" y="312">nullam hilit, temporr oriates</text>
      <text x="679" y="324">nes sed untor si tem quisq</text>
    </g>

    <!-- Hotelmietwäsche -->
    <text x="953" y="219" class="serif" font-size="16.5" fill="var(--gold)">Hotelmietwasche</text>
    <g class="body-copy" fill="var(--lavender-light)" font-size="10">
      <text x="950" y="246">In Ihrem Hotel erwartet Ihre Gäste</text>
      <text x="950" y="258">exklusives Ambiente, eine gute</text>
      <text x="950" y="270">Küche und eine herzliche Atmo-</text>
      <text x="950" y="282">sphäre.</text>
      <text x="950" y="294">Gerne unterstützen wir Sie hier mit</text>
      <text x="950" y="306">unseren Dienstleistungen aus der</text>
      <text x="950" y="318">hygienezertifizierten Wäscherei.</text>
    </g>
  </svg>

  <!-- Back cover -->
  <svg class="page back" viewBox="0 0 596 420" xmlns="http://www.w3.org/2000/svg">
    <rect width="596" height="420" fill="var(--navy)"/>
    <polygon points="64,32 70,20 82,20 88,32 82,44 70,44" fill="var(--lavender)"/>
    <polygon points="108,57 114,46 128,46 134,57 128,68 114,68" fill="var(--lavender)"/>
    <polygon points="157,31 161,24 169,24 173,31 169,38 161,38" fill="var(--hex-blue)"/>
    <polygon points="0,55 27,55 50,95 27,150 0,150" fill="var(--lavender)" opacity=".85"/>
    <polygon points="30,80 42,55 70,55 80,80 70,105 42,105" fill="var(--hex-blue)" opacity=".85"/>
    <polygon points="52,170 76,108 140,108 164,170 140,232 76,232" fill="var(--lavender)" opacity=".85"/>
    <polygon points="132,177 145,145 175,145 189,177 175,208 145,208" fill="#8f98c2" opacity=".7"/>
    <polygon points="225,172 233,155 252,155 260,172 252,189 233,189" fill="var(--lavender)"/>
    <polygon points="0,162 48,162 80,248 0,248" fill="#857c5c" opacity=".85"/>
    <polygon points="108,245 116,228 136,228 144,245 136,262 116,262" fill="#8f98c2" opacity=".7"/>
    <polygon points="0,248 222,248 596,408 596,420 0,420" fill="var(--lime)"/>
    <polygon points="0,248 85,248 60,335 0,335" fill="var(--yellow)"/>
    <polygon points="505,305 517,285 541,285 553,305 541,325 517,325" fill="var(--hex-blue)"/>
    <polygon points="506,305 513,292 529,292 536,305 529,318 513,318" fill="var(--lavender)" opacity=".85"/>
    <rect x="63" y="283" width="3" height="137" fill="var(--navy)"/>
    <circle cx="317" cy="150" r="22" fill="none" stroke="var(--white)" stroke-width="4"/>
    <text x="350" y="158" class="brand-name" font-size="22" fill="var(--white)">Wäscherei Kranzbeck</text>
    <g class="sans" font-size="10.5" fill="var(--ink)">
      <text x="77" y="292">Address Here Address Here Address</text>
      <text x="77" y="306">Here Address Here.</text>
      <text x="77" y="324">Phone: +1234656 7890, Fax: +123 456 7890</text>
      <text x="77" y="342">Profil: www.netzprofil.example/userid,</text>
      <text x="77" y="356">Kurznews: www.kurznews.example/userid</text>
      <text x="77" y="374">Email: mymailid@domain.com</text>
      <text x="77" y="388">Website: mywebsite.com</text>
    </g>
  </svg>

</div>
</body>
</html>
```